Event Poster - Tarawera Mist Fest 2018 (Need ASAP)

Create a poster for an upcoming vape event, located in Waikato, Hamilton, New Zealand.

Mist Fest is an event where lots of shops come to a location, and the public are welcomed and they all vape, buy vape products, socialize, drink beer and have fun.

VISIT THE EVENT WEBSITE FOR INFO - www.taraweramistfest.co.nz

We have created a website at, as you can see the logo and design is a bit boring and plain, so we dont really want it to look anything like that, The logo that is created to suit the poster will be able to be

Need a poster done up so we can send it around, post it up on boards, share on social media etc

I have attached previous events from nearby towns, for reference, but I want something much better.

Target Market(s)

25-45 Male / Female

Requirements
Must have
• - Tarawera Mist Fest 2018
• - Saturday, 2nd June 2018
• - 12-10pm
• - R18 Event (important for public to know)
• - Vendors, Prizes, Comps, Cloud Liquid Medals, Entertainment, Giveaways & More
• - The Corner Alehouse (14 Moller Ln, Kopuku, Hamilton)
• - mention something along lines "Join Tarawera's Opening Mist Fest"
• - "Grab Your Passes at www.taraweramistfest.co.nz NOW"
• - I want people to know they can buy it from a store as well "The Haze Hut"
Nice to have
• Our City colors are Red,Yellow,Black which is symbolic for "Waikato" so it would be nice to have those integrated in there. Alot of the other Mist Fest events have dark, bogan, amateur look done to them, so I want ours to be just a much better version.
• To Clarify, Hamilton is a city inside the Waikato
• I might want to put sponsors on there as well, possibly 10-20, but maybe only a few if space is a problem

```html
<!DOCTYPE html>
<html lang="en">
<head>
<meta charset="utf-8">
<title>Tarawera Mist Fest 2018 — Event Poster</title>
<link rel="stylesheet" href="https://fonts.googleapis.com/css2?family=Abril+Fatface&family=Oswald:wght@300&family=Passion+One:wght@700&family=Prata&display=swap">
<style>
  :root {
    --ink: #050505;
    --paper: #ffffff;
    --tile: #f2f2f2;
    --red: #e31b1b;
    --stamp: #c8161b;
    --flame-hot: #b3130f;
    --gold: #f5c400;
  }
  * { margin: 0; padding: 0; box-sizing: border-box; }
  html, body { width: 848px; height: 1200px; overflow: hidden; background: var(--ink); }
  .poster {
    position: relative;
    width: 848px;
    height: 1200px;
    overflow: hidden;
    background: var(--ink);
    color: var(--paper);
    font-family: "Prata", serif;
  }
  .flames {
    position: absolute;
    left: 120px; top: 480px;
    width: 728px; height: 720px;
    background:
      radial-gradient(ellipse 45% 30% at 40% 95%, var(--flame-hot) 0%, rgba(179,19,15,0.6) 40%, transparent 75%),
      radial-gradient(ellipse 30% 55% at 45% 55%, rgba(120,10,8,0.75) 0%, rgba(90,6,6,0.4) 50%, transparent 80%),
      radial-gradient(ellipse 20% 35% at 70% 40%, rgba(90,6,6,0.5) 0%, transparent 80%);
  }
  .title {
    position: absolute;
    top: 66px; left: 0; width: 100%;
    text-align: center;
    font-family: "Passion One", sans-serif;
    font-weight: 700;
    font-size: 66px;
    line-height: 1;
    color: var(--paper);
    -webkit-text-stroke: 10px var(--red);
    paint-order: stroke fill;
  }
  .tagline {
    position: absolute;
    top: 164px; left: 0; width: 100%;
    text-align: center;
    font-size: 28px; line-height: 1;
  }
  .date { position: absolute; top: 240px; left: 0; width: 100%; height: 97px; }
  .tile {
    position: absolute; top: 0; height: 97px;
    background: var(--tile);
    display: flex; justify-content: space-around; align-items: center;
    font-family: "Oswald", sans-serif; font-weight: 300;
    font-size: 86px; line-height: 1; color: #111;
    padding: 0 6px;
  }
  .tile::after {
    content: ""; position: absolute; left: 0; right: 0; top: 48px;
    height: 1px; background: #9a9a9a;
  }
  .tile--day { left: 68px; width: 168px; }
  .tile--num { left: 263px; width: 57px; }
  .tile--month { left: 347px; width: 169px; }
  .tile--year { left: 553px; width: 225px; }
  .time {
    position: absolute; left: 55px; top: 398px;
    font-size: 48px; line-height: 1; white-space: nowrap;
  }
  .stamp {
    position: absolute;
    border: 5px solid var(--stamp);
    border-radius: 14px;
    color: var(--stamp);
    font-family: "Abril Fatface", serif;
    text-align: center;
  }
  .stamp__inner {
    position: absolute; inset: 7px;
    border: 5px solid var(--stamp);
    border-radius: 10px;
  }
  .stamp--age { left: 438px; top: 376px; width: 356px; height: 180px; }
  .stamp--age .age {
    position: absolute; top: 22px; left: 0; width: 100%;
    font-size: 54px; line-height: 1;
    display: flex; justify-content: center; align-items: center; gap: 38px;
  }
  .star { width: 44px; height: 44px; fill: var(--stamp); }
  .stamp--age .adults {
    position: absolute; top: 90px; left: 0; width: 100%;
    font-size: 50px; line-height: 1; white-space: nowrap;
  }
  .features {
    position: absolute; left: 68px; top: 518px;
    font-size: 37px; line-height: 48px;
  }
  .pin { position: absolute; left: 42px; top: 706px; width: 79px; height: 119px; }
  .address {
    position: absolute; left: 137px; top: 684px;
    font-family: "Abril Fatface", serif;
    font-size: 46px; line-height: 52px; white-space: nowrap;
  }
  .ticket { position: absolute; left: 52px; top: 856px; width: 156px; height: 79px; }
  .web {
    position: absolute; left: 220px; top: 878px;
    font-size: 30px; line-height: 1; white-space: nowrap;
  }
  .stamp--shop { left: 50px; top: 970px; width: 510px; height: 179px; opacity: 0.85; }
  .stamp--shop p {
    position: absolute; left: 0; width: 100%;
    font-size: 48px; line-height: 1; white-space: nowrap;
  }
  .stamp--shop .avail { top: 36px; }
  .stamp--shop .shop { top: 96px; }
  .brand {
    position: absolute; left: 589px; top: 962px; width: 205px; height: 175px;
    background: var(--paper);
    display: flex; align-items: center; gap: 10px; padding: 0 14px;
  }
  .brand__mark { width: 34px; height: 34px; background: var(--gold); flex: none; }
  .brand__name {
    font-family: "Prata", serif; color: var(--ink);
    font-size: 22px; line-height: 1.15; text-transform: uppercase;
  }
</style>
</head>
<body>
<main class="poster">
  <div class="flames" role="img" aria-label="Red flames rising from the bottom of the poster"></div>

  <h1 class="title">Tarawera Mist Fest 2018</h1>
  <p class="tagline">Join Tarawera's Opening Mist Fest</p>

  <div class="date" aria-label="Saturday 2 June 2018">
    <div class="tile tile--day"><span>S</span><span>A</span><span>T</span></div>
    <div class="tile tile--num"><span>2</span></div>
    <div class="tile tile--month"><span>J</span><span>U</span><span>N</span></div>
    <div class="tile tile--year"><span>2</span><span>0</span><span>1</span><span>8</span></div>
  </div>

  <p class="time">Time 12-10pm</p>

  <div class="stamp stamp--age">
    <div class="stamp__inner"></div>
    <div class="age">
      <svg class="star" viewBox="0 0 24 24"><polygon points="12,1 14.9,8.6 23,9 16.7,14.1 18.8,22 12,17.6 5.2,22 7.3,14.1 1,9 9.1,8.6"/></svg>
      <span>18+</span>
      <svg class="star" viewBox="0 0 24 24"><polygon points="12,1 14.9,8.6 23,9 16.7,14.1 18.8,22 12,17.6 5.2,22 7.3,14.1 1,9 9.1,8.6"/></svg>
    </div>
    <p class="adults">Adults only</p>
  </div>

  <p class="features">Vendors, Prizes,<br>Comps, Cloud Liquid Medals,<br>Entertaiment, Giveaways and More</p>

  <svg class="pin" viewBox="0 0 79 119" aria-hidden="true">
    <path d="M39.5 2C18.5 2 2 18 2 39c0 27 37.5 78 37.5 78S77 66 77 39C77 18 60.5 2 39.5 2z" fill="var(--red)"/>
    <circle cx="39.5" cy="38" r="18" fill="var(--ink)"/>
    <path d="M22 70 L39.5 96 L57 70 L50 70 L39.5 86 L29 70z" fill="var(--paper)"/>
  </svg>
  <p class="address">The Corner Alehouse,<br>14 Moller Ln,<br>Kopuku, Hamilton</p>

  <svg class="ticket" viewBox="0 0 156 79" aria-label="Event ticket">
    <path d="M6 4h144v18a6 6 0 0 0 0 12v11a6 6 0 0 0 0 12v18H6V57a6 6 0 0 0 0-12V34a6 6 0 0 0 0-12z" fill="#f4e3c8" stroke="var(--red)" stroke-width="5"/>
    <rect x="16" y="12" width="124" height="55" fill="none" stroke="var(--red)" stroke-width="2"/>
    <text x="78" y="37" text-anchor="middle" font-family="Abril Fatface, serif" font-size="21" fill="#111">EVENT</text>
    <text x="78" y="61" text-anchor="middle" font-family="Prata, serif" font-size="20" fill="#111">TICKET</text>
  </svg>
  <p class="web">www.taraweramistfest.co.nz TODAY</p>

  <div class="stamp stamp--shop">
    <div class="stamp__inner"></div>
    <p class="avail">Available Now</p>
    <p class="shop">"The Haze Hut"</p>
  </div>

  <div class="brand">
    <span class="brand__mark"></span>
    <span class="brand__name">Tarawera<br>Mist Fest<br>2018</span>
  </div>
</main>
</body>
</html>
```